Velisto Events Business Card

We need a business cards that stands out to our clients. We are company who targets prestige clients to spend money with us on experiences, so our image needs to be prestige
Target Market(s)
Corporate
Contact Information for Business Card
There will be four different names on the business cards
Dana Morrowby
Director
O: 02 5147 3086
M: 0451 692 038
E: info@velistoevents.example.au
Facebook: @velistoevents
Instagram: velistoevents
www.velistoevents.example.au
Nathaniel Morrowby
Director
O: 02 5147 3086
M: 0467 215 904
Facebook: @velistoevents
Instagram: velistoevents
www.velistoevents.example.au
Teodor Vinkel
Director
O: 02 5147 3086
M: 0478 903 527
Facebook: @velistoevents
Instagram: velistoevents
www.velistoevents.example.au
Mabel Hartung
Director
O: 02 5147 3086
Facebook: @velistoevents
Instagram: velistoevents
www.velistoevents.example.au
Colors
Designer to choose colors to be used in the design.
Look and feel

```html
<!DOCTYPE html>
<html lang="en">
<head>
<meta charset="utf-8">
<title>Velisto Events Business Card</title>
<link rel="stylesheet" href="https://fonts.googleapis.com/css2?family=Cinzel:wght@500;700&family=Open+Sans:wght@400&display=swap">
<style>
  :root {
    --backdrop: #1c1d22;
    --card-navy: #2b2766;
    --card-navy-deep: #221f55;
    --gold: #d9ab45;
    --gold-soft: #c99a3a;
  }
  * { box-sizing: border-box; margin: 0; padding: 0; }
  html, body {
    width: 1200px;
    height: 900px;
    overflow: hidden;
    background: var(--backdrop);
  }
  .canvas {
    width: 1200px;
    height: 900px;
    display: flex;
    align-items: center;
    justify-content: center;
    gap: 60px;
  }
  .card {
    position: relative;
    width: 520px;
    height: 300px;
    border-radius: 26px;
    background: linear-gradient(135deg, var(--card-navy) 0%, var(--card-navy-deep) 100%);
    color: var(--gold);
    box-shadow: 0 18px 40px rgba(0, 0, 0, 0.45);
  }
  /* Front: contact side */
  .card-front .contact-block {
    position: absolute;
    left: 38px;
    top: 34px;
    font-family: "Open Sans", sans-serif;
  }
  .person-name {
    font-family: "Cinzel", serif;
    font-weight: 700;
    font-size: 21px;
    letter-spacing: 0.5px;
    color: var(--gold);
    line-height: 1.1;
  }
  .person-role {
    font-size: 14px;
    color: var(--gold-soft);
    margin-top: 4px;
  }
  .divider {
    width: 16px;
    height: 2px;
    background: var(--gold);
    margin: 20px 0 22px;
  }
  .contact-list {
    list-style: none;
    font-size: 14px;
    line-height: 1.5;
    color: var(--gold);
  }
  .social-line {
    display: flex;
    align-items: center;
    gap: 8px;
    margin-top: 2px;
  }
  .social-dot {
    width: 13px;
    height: 13px;
    border-radius: 50%;
    background: var(--gold);
  }
  .front-wordmark {
    position: absolute;
    right: 40px;
    top: 50%;
    transform: translateY(-50%);
    width: 170px;
    text-align: center;
    font-family: "Cinzel", serif;
    font-weight: 500;
    font-size: 26px;
    line-height: 1.3;
    letter-spacing: 3px;
    color: var(--gold);
  }
  /* Back: brand side */
  .card-back {
    display: flex;
    align-items: center;
    justify-content: center;
  }
  .back-wordmark {
    font-family: "Cinzel", serif;
    font-weight: 500;
    font-size: 30px;
    letter-spacing: 6px;
    color: var(--gold);
  }
</style>
</head>
<body>
  <main class="canvas">
    <section class="card card-front" aria-label="Business card front">
      <div class="contact-block">
        <h1 class="person-name">Dana Morrowby</h1>
        <p class="person-role">Director</p>
        <div class="divider"></div>
        <ul class="contact-list">
          <li>0451 692 038</li>
          <li>info@velistoevents.example.au</li>
          <li>www.velistoevents.example.au</li>
          <li class="social-line"><span class="social-dot"></span>@velistoevents</li>
        </ul>
      </div>
      <div class="front-wordmark">Velisto Events</div>
    </section>

    <section class="card card-back" aria-label="Business card back">
      <div class="back-wordmark">Velisto Events</div>
    </section>
  </main>
</body>
</html>
```